ALL I NEED IS A BUSINESS CARD AND LETTER HEAD OFFICIAL PAPER

i only need a letter head ( sample attached)
along with business cards.
i will upload a sample ,along with the logo of both companies that should be on the letter head and business cards.

Note:its a high end maritime solution company

Company name is Haldwick Norcrest Africa

slogan : For maritime solution ( it could be on the back side of the business card)
Updates

Project Deadline Extended Reason: Hi Guys, thanks for your designs , i am sorry but now we just changed the company name toLuerssen Norcrest Africa slogan For Maritime solutions. i hope you can help me with that! slogan could be in the back side or any place, but not next to the title . and both logos of norcrest and haldwik should be there. thank you Added Sunday, March 1, 2015

Industry/Entity Type

Business

Contact Information for Business Card

as attached, please provide more designs

Font styles to use
Serif

Requirements
Must have
• SAME AS THE BUSINESS LETTER,
• Haldwick Norcrest Africa
• slogan for Maritime Solutions

```html
<!DOCTYPE html>
<html lang="en">
<head>
<meta charset="utf-8">
<title>Haldwick Norcrest Africa — Letterhead</title>
<link rel="stylesheet" href="https://fonts.googleapis.com/css2?family=EB+Garamond:wght@400;600;700&display=swap">
<style>
  :root {
    --page: #ffffff;
    --rule-blue: #0b5fc4;
    --brand-grey: #8a98ad;
    --brand-navy: #123f8c;
    --wave-light: #1c8ff0;
    --wave-deep: #0a4a9e;
    --band-grey: #d4d6da;
    --band-fade: #f2f3f5;
    --ink: #1b1b1b;
    --ink-light: #ffffff;
  }
  * { margin: 0; padding: 0; box-sizing: border-box; }
  html, body { width: 849px; height: 1200px; overflow: hidden; background: var(--page); }
  .letterhead {
    position: relative;
    width: 849px;
    height: 1200px;
    background: var(--page);
    font-family: "EB Garamond", "Times New Roman", serif;
    overflow: hidden;
  }
  .top-rule {
    position: absolute; top: 0; left: 0; right: 0;
    height: 3px;
    background: linear-gradient(90deg, var(--rule-blue), #5aa6ee 60%, var(--rule-blue));
  }
  .brand-row {
    position: absolute; top: 28px; left: 20px;
    display: flex; align-items: center; gap: 18px;
  }
  .brand-primary {
    font-size: 27px; font-weight: 700; letter-spacing: 0.5px;
    color: var(--brand-grey);
  }
  .brand-secondary { display: flex; align-items: center; gap: 8px; }
  .brand-mark { width: 34px; height: 34px; background: var(--brand-navy); }
  .brand-secondary-name {
    font-size: 20px; font-weight: 700; letter-spacing: 0.5px;
    color: var(--brand-navy);
  }
  .footer-wave { position: absolute; left: 0; bottom: 0; width: 849px; height: 1200px; }
  .contact-line {
    position: absolute; top: 1148px;
    font-size: 17px; white-space: nowrap;
  }
  .contact-web { left: 48px; color: var(--ink-light); }
  .contact-email { left: 366px; color: var(--ink); }
  .contact-tel { left: 659px; color: var(--ink); }
</style>
</head>
<body>
  <main class="letterhead">
    <div class="top-rule"></div>

    <header class="brand-row">
      <span class="brand-primary">HALDWIK</span>
      <span class="brand-secondary">
        <span class="brand-mark"></span>
        <span class="brand-secondary-name">NORCREST</span>
      </span>
    </header>

    <svg class="footer-wave" viewBox="0 0 849 1200" aria-hidden="true">
      <defs>
        <linearGradient id="band-grad" x1="0" y1="0" x2="1" y2="1">
          <stop offset="0" stop-color="var(--band-grey)"/>
          <stop offset="1" stop-color="var(--band-fade)"/>
        </linearGradient>
        <linearGradient id="wave-grad" x1="0" y1="0" x2="1" y2="1">
          <stop offset="0" stop-color="var(--wave-light)"/>
          <stop offset="1" stop-color="var(--wave-deep)"/>
        </linearGradient>
      </defs>
      <path d="M0,781 C70,1000 250,1160 432,1200 L0,1200 Z" fill="url(#band-grad)"/>
      <path d="M0,862 C80,1030 230,1160 382,1200 L0,1200 Z" fill="url(#wave-grad)"/>
    </svg>

    <footer>
      <p class="contact-line contact-web">www.haldwiknorcrest.com</p>
      <p class="contact-line contact-email">Email: info@haldwiknorcrest.com</p>
      <p class="contact-line contact-tel">Tel: (021) 555-0147</p>
    </footer>
  </main>
</body>
</html>
```